An update to our current wine label

we want to freshen up our current wine label. we have changed it already into a wrap label that is one piece, but we need something that pops a little more. the logo is a bit plain and we plan on raised peinting the Wine stain part of the logo. i wpuld love to have it be huge covering the label, but i cant lose anybofbthe inportant info written on the label either. so im not sure what to do at this point.

```html
<!DOCTYPE html>
<html lang="en">
<head>
<meta charset="utf-8">
<title>Stillbrook Vineyards – Marlow's Red Wrap Label</title>
<link rel="stylesheet" href="https://fonts.googleapis.com/css2?family=Cinzel:wght@400;700&family=Crimson+Text:wght@400;600&family=Roboto+Condensed:wght@400;700&family=Open+Sans:wght@400;600&display=swap">
<style>
  :root {
    --page-bg: #e4e4e4;
    --cream: #fbf7ef;
    --peach: #f6e8d2;
    --mist: #b9c1d1;
    --ridge-mid: #737e98;
    --ridge-dark: #474d60;
    --night: #2f3446;
    --wine: #a8232a;
    --stain: #a04f60;
    --ink: #2c3040;
    --white: #ffffff;
  }
  * { margin: 0; padding: 0; box-sizing: border-box; }
  html, body { width: 1200px; height: 995px; overflow: hidden; }
  body { background: var(--page-bg); position: relative; }

  .label {
    position: absolute; left: 25px; top: 78px;
    width: 1150px; height: 838px; overflow: hidden;
  }
  .label-backdrop {
    position: absolute; inset: 0;
    background: linear-gradient(to bottom,
      var(--cream) 0%, var(--peach) 30%, var(--cream) 50%,
      var(--mist) 57%, var(--ridge-mid) 65%, var(--ridge-dark) 75%,
      var(--night) 86%, #3c4152 100%);
  }

  .brand {
    position: absolute; left: 168px; top: 88px; width: 480px;
    font-family: "Cinzel", serif; font-weight: 700; color: var(--wine);
    text-align: center; line-height: 0.95;
  }
  .brand-line-1 { font-size: 122px; display: block; }
  .brand-line-2 { font-size: 108px; display: block; }
  .brand-line-3 { font-size: 50px; display: block; letter-spacing: 3px; margin-top: 10px; }
  .brand-ring {
    position: absolute; left: 643px; top: 99px; width: 396px; height: 396px;
    border-radius: 50%; border: 18px solid var(--stain);
  }

  .contact {
    position: absolute; left: 14px; top: 33px; height: 380px;
    writing-mode: vertical-rl; color: var(--ink);
    font-family: "Open Sans", sans-serif;
  }
  .contact .web { font-size: 14px; line-height: 24px; font-weight: 600; }
  .contact .producer { font-family: "Roboto Condensed", sans-serif; font-size: 10.5px; line-height: 15px; text-transform: uppercase; }

  .warning {
    position: absolute; left: 18px; top: 477px; height: 345px;
    writing-mode: vertical-rl; color: var(--white);
    font-family: "Roboto Condensed", sans-serif; font-size: 11.5px; line-height: 17px;
  }
  .warning strong { font-weight: 700; }

  .tasting-note {
    position: absolute; left: 1012px; top: 481px; height: 335px; width: 130px;
    writing-mode: vertical-rl; transform: rotate(180deg);
    color: var(--white); font-family: "Open Sans", sans-serif;
    font-size: 13.5px; line-height: 20.5px;
  }

  .wine-info { position: absolute; left: 0; width: 1150px; color: var(--white); text-align: center; }
  .vintage { top: 571px; font-family: "Crimson Text", serif; font-size: 34px; letter-spacing: 5px; left: -68px; }
  .designation { top: 613px; font-family: "Crimson Text", serif; font-size: 29px; left: -68px; }
  .wine-name { top: 650px; font-family: "Cinzel", serif; font-size: 52px; letter-spacing: 6px; left: -68px; }
  .region { top: 711px; font-family: "Crimson Text", serif; font-size: 24px; left: -68px; }

  .rule { position: absolute; left: 193px; top: 749px; width: 765px; height: 4px; background: var(--wine); }

  .spec { position: absolute; color: var(--white); font-family: "Crimson Text", serif; font-size: 23px; line-height: 25px; }
  .spec-type { left: 296px; top: 759px; }
  .spec-volume { right: 291px; top: 759px; text-align: right; }
</style>
</head>
<body>
  <main class="label">
    <div class="label-backdrop" role="img" aria-label="Misty layered blue mountain ridges beneath a pale dawn sky"></div>

    <div class="brand">
      <span class="brand-line-1">STILL</span>
      <span class="brand-line-2">BROOK</span>
      <span class="brand-line-3">VINEYARDS</span>
    </div>
    <div class="brand-ring"></div>

    <div class="contact">
      <p class="web">www.stillbrookvineyards.com</p>
      <p class="web">@stillbrookwinery</p>
      <p class="producer">Produced and bottled by Stillbrook Vineyard LLC</p>
      <p class="producer">2140 Stillbrook Rd. Alder Creek, TN 37000</p>
    </div>

    <div class="warning">
      <p><strong>GOVERNMENT WARNING:</strong></p>
      <p>(1) According to the Surgeon General, women should not drink alcoholic beverages during pregnancy because of the risk of birth defects.</p>
      <p>(2) Consumption of alcoholic beverages impairs your ability to drive a car or operate machinery, and may cause health problems.</p>
    </div>

    <p class="tasting-note">A dry red blend of rich, mid-bodied grape. The Marquette grape is a lighter bodied and is blended with a heavier European grape. It is then aged 18 months on French oak from the Loire Valley. It has aromas of dark cherries and currants.</p>

    <p class="wine-info vintage">2023</p>
    <p class="wine-info designation">ESTATE BOTTLED</p>
    <h1 class="wine-info wine-name" style="font-weight:400">MARLOW’S RED</h1>
    <p class="wine-info region">COCKE COUNTY</p>

    <div class="rule"></div>

    <p class="spec spec-type">Red Wine</p>
    <p class="spec spec-volume">13% ALC./VOL.<br>750 ML</p>
  </main>
</body>
</html>
```